Dalvor Inc Business Card

Looking to get an updated business card for a Contract Machining company (www.dalvorinc-example.com) - looking for a clean design the portrays the technical nature of the business - colors can follow the website design and be in any combination that makes sense (red black, white, metallic or silver) - logos attached for use also. Would like space for: Name, title, business phone (555 214-3098), cell phone , website (www.dalvorinc-example.com) - possibly QR code could be integrated for website (designer choice), business address - 418 Birchfield Lane, Alder Falls, MI 48592 (cards will be for 4 employees, I will either need to modify a template or I can provide individual information)
Target Market(s)
Aerospace, defense and medical device manufacturing companies that need machining
Industry/Entity Type
Machining for aerospace, defense, medical
Contact Information for Business Card
Name, Title, Business Phone, Cell Phone, email, business website and business address

```html
<!DOCTYPE html>
<html lang="en">
<head>
<meta charset="utf-8">
<title>Dalvor Inc Business Card</title>
<link rel="stylesheet" href="https://fonts.googleapis.com/css2?family=Montserrat:wght@400;500;600;700&display=swap">
<style>
  :root {
    --brand-red: #b01e24;
    --paper: #ffffff;
    --ink: #1f1f1f;
    --backdrop: #c6c3c4;
  }
  * { margin: 0; padding: 0; box-sizing: border-box; }
  html, body {
    width: 1200px; height: 1200px; overflow: hidden;
    background: var(--backdrop);
    font-family: "Montserrat", sans-serif;
  }
  .card {
    position: absolute; left: 151px; width: 897px; height: 525px;
    background: var(--paper);
    overflow: hidden;
  }
  .card--front { top: 51px; }
  .card--back { top: 624px; }

  .front-band {
    position: absolute; left: 186px; top: 50px;
    width: 711px; height: 276px;
    background: var(--brand-red);
  }
  .front-badge {
    position: absolute; left: 54px; top: 54px;
    width: 268px; height: 268px; border-radius: 50%;
    background: var(--brand-red);
  }
  .front-badge__disc {
    position: absolute; left: 14px; top: 14px;
    width: 240px; height: 240px; border-radius: 50%;
    background: var(--paper);
    display: flex; align-items: center; justify-content: center;
  }
  .brand-name {
    color: var(--brand-red);
    font-weight: 700;
    letter-spacing: 1px;
    line-height: 1;
  }
  .front-badge .brand-name { font-size: 30px; }

  .holder {
    position: absolute; right: 63px; top: 160px;
    text-align: right; color: var(--paper);
  }
  .holder__name { font-size: 37px; font-weight: 600; letter-spacing: 1px; line-height: 1; }
  .holder__title { font-size: 20px; font-weight: 400; margin-top: 16px; line-height: 1; letter-spacing: .5px; }

  .contact-list {
    position: absolute; right: 60px; top: 352px;
    list-style: none;
  }
  .contact-list li {
    display: flex; align-items: center; justify-content: flex-end;
    height: 41px; font-size: 21px; color: var(--ink); font-weight: 400;
    letter-spacing: .3px;
  }
  .contact-list svg { width: 22px; height: 22px; margin-left: 20px; }

  .back-mark {
    position: absolute; left: 326px; top: 98px;
    width: 245px; height: 245px; border-radius: 50%;
    background: var(--brand-red);
  }
  .back-wordmark {
    position: absolute; left: 0; width: 100%; top: 356px;
    text-align: center;
  }
  .back-wordmark .brand-name { display: block; font-size: 50px; letter-spacing: 2px; }
  .back-wordmark .brand-suffix {
    display: block; color: var(--brand-red);
    font-size: 21px; font-weight: 500; margin-top: 6px; letter-spacing: 1.5px;
  }
</style>
</head>
<body>
  <section class="card card--front">
    <div class="front-band"></div>
    <div class="front-badge">
      <div class="front-badge__disc"><span class="brand-name">DALVOR</span></div>
    </div>
    <div class="holder">
      <div class="holder__name">TOBIAS HALLGREN</div>
      <div class="holder__title">Director</div>
    </div>
    <ul class="contact-list">
      <li>555 214-3098
        <svg viewBox="0 0 24 24" aria-hidden="true"><path fill="var(--brand-red)" d="M6.6 10.8a15.1 15.1 0 0 0 6.6 6.6l2.2-2.2c.3-.3.7-.4 1-.2 1.1.4 2.3.6 3.6.6.6 0 1 .4 1 1V20c0 .6-.4 1-1 1C10.6 21 3 13.4 3 4c0-.6.4-1 1-1h3.5c.6 0 1 .4 1 1 0 1.3.2 2.5.6 3.6.1.3 0 .7-.2 1z"/></svg>
      </li>
      <li>www.dalvorinc-example.com
        <svg viewBox="0 0 24 24" aria-hidden="true"><rect x="3" y="5" width="18" height="14" rx="1.5" fill="var(--brand-red)"/><path d="M4.5 7l7.5 6 7.5-6" fill="none" stroke="#fff" stroke-width="1.6"/></svg>
      </li>
      <li>418 Birchfield Lane, Alder Falls, MI 48592
        <svg viewBox="0 0 24 24" aria-hidden="true"><circle cx="12" cy="12" r="9" fill="none" stroke="var(--brand-red)" stroke-width="1.8"/><ellipse cx="12" cy="12" rx="4" ry="9" fill="none" stroke="var(--brand-red)" stroke-width="1.5"/><path d="M3 12h18M5 7.5h14M5 16.5h14" stroke="var(--brand-red)" stroke-width="1.5" fill="none"/></svg>
      </li>
    </ul>
  </section>

  <section class="card card--back">
    <div class="back-mark"></div>
    <div class="back-wordmark">
      <span class="brand-name">DALVOR</span>
      <span class="brand-suffix">INC.</span>
    </div>
  </section>
</body>
</html>
```